Law Firm Website

We are looking to update our old, tired and very flat website. We have someone who will code and host the site but we need some design inspiration. The website will consist of no more than 2/3 pages, possibly with pop-ups for information. We already have all the blurb. We would like something distinctive, clean and eye-catching, using the purple and white theme that we already use on our firm stationery. Examples uploaded. Current website URL is www.dunmorewillett.example.

Industry/Entity Type

Law Firm

```html
<!DOCTYPE html>
<html lang="en">
<head>
<meta charset="utf-8">
<title>Dunmore &amp; Willett Solicitors</title>
<link rel="stylesheet" href="https://fonts.googleapis.com/css2?family=Cinzel:wght@400&family=Slabo+27px&display=swap">
<style>
:root{
  --ink-dark:#222226;
  --purple:#5b3f86;
  --purple-band:rgba(86,58,128,.92);
  --purple-text:#5a3f8a;
  --paper:#f3f2ef;
  --text:#444;
  --muted:#8a8a8e;
  --white:#fff;
}
*{margin:0;padding:0;box-sizing:border-box}
html,body{width:1200px;height:1010px;overflow:hidden}
body{position:relative;background:var(--paper);font-family:Arial,Helvetica,sans-serif;color:var(--text)}
.site-header{position:absolute;left:0;top:0;width:1200px;height:109px;background:var(--ink-dark);border-bottom:4px solid var(--purple)}
.brand{position:absolute;left:100px;top:36px;color:#d4d4d8;font-family:"Slabo 27px",serif;font-size:27px;line-height:32px}
.main-nav{position:absolute;right:100px;top:63px;display:flex;gap:45px;font-family:"Slabo 27px",serif;font-size:17px}
.main-nav a{color:#d4d4d8;text-decoration:none;position:relative}
.main-nav a.active::after{content:"";position:absolute;left:50%;top:32px;margin-left:-12px;border:12px solid transparent;border-bottom:8px solid var(--purple);border-top:0}
.hero{position:absolute;left:0;top:109px;width:1200px;height:303px;background:linear-gradient(180deg,#b9bdd2 0%,#d8d6df 45%,#e6e2e8 100%)}
.hero-title{position:absolute;left:0;top:247px;width:1200px;text-align:center;font-family:"Cinzel",serif;font-weight:400;font-size:33px;color:var(--purple-text);letter-spacing:1px}
.hero-tagline{position:absolute;left:0;top:290px;width:1200px;text-align:center;font-family:"Slabo 27px",serif;font-size:22px;letter-spacing:2px;color:#444}
.partners-band{position:absolute;left:0;top:412px;width:1200px;height:152px;background:rgba(86,58,128,.8)}
.partners-inner{position:absolute;left:100px;top:0;width:1000px;height:152px;background:var(--purple-band)}
.portrait{position:absolute;top:8px;width:118px;height:136px;border:5px solid var(--white);background:linear-gradient(160deg,#9a9a9a,#3a3a3a)}
.partner{position:absolute;top:22px;color:#d9d3e6;font-size:14px;line-height:17px}
.partner h3{font-family:"Slabo 27px",serif;font-weight:normal;font-size:19px;color:var(--white);margin-bottom:4px}
.partner .btn{position:absolute;top:96px;width:117px;height:26px;background:var(--white);color:#333;font-family:"Slabo 27px",serif;font-size:14px;line-height:26px;text-align:center;text-decoration:none}
.partner-left{left:133px}
.partner-left .btn{left:1px}
.partner-right{right:134px;text-align:right}
.partner-right .btn{right:0}
.regulation{position:absolute;left:280px;top:58px;width:440px;text-align:center;color:var(--white);font-family:"Slabo 27px",serif;font-size:17px;line-height:20px}
.expertise{position:absolute;left:100px;top:607px;width:1000px}
.expertise h2{font-family:"Slabo 27px",serif;font-weight:normal;font-size:23px;color:#333;text-align:center;padding-bottom:4px;border-bottom:1px solid #aaa}
.expertise-list{position:absolute;top:54px;list-style:none;font-size:14px;line-height:28px;color:#555}
.expertise-list li::before{content:"• "}
.site-footer{position:absolute;left:0;top:814px;width:1200px;height:196px;background:var(--ink-dark);text-align:center;color:var(--muted);font-size:14.5px}
.site-footer .legal{margin-top:17px;line-height:17px}
.site-footer a{color:#7a5fb0;text-decoration:none}
.member-badge{display:block;width:154px;height:57px;background:var(--white);margin:16px auto 0}
.footer-links{margin-top:12px;font-size:12px}
.footer-links a{color:var(--muted)}
.copyright{margin-top:12px;font-size:14.5px}
</style>
</head>
<body>
<header class="site-header">
  <div class="brand">Dunmore &amp; Willett</div>
  <nav class="main-nav">
    <a class="active" href="#">Home</a><a href="#">Areas of Expertise</a><a href="#">Daniel Dunmore</a><a href="#">Peter Willett</a><a href="#">Contact</a>
  </nav>
</header>

<section class="hero" role="img" aria-label="Soft-focus photograph of a Victorian gothic building with turrets against a pale sky"></section>
<h1 class="hero-title">DUNMORE &amp; WILLETT SOLICITORS</h1>
<p class="hero-tagline">FOR THE SERVICE YOU DESERVE</p>

<section class="partners-band">
  <div class="partners-inner">
    <div class="portrait" style="left:8px" role="img" aria-label="Black and white portrait photograph of Daniel Dunmore"></div>
    <div class="partner partner-left">
      <h3>Daniel Dunmore</h3>
      22b Elmfield Row<br>Northcote<br>London NX9 4QT<br>Tel: 0300 555 0142
      <a class="btn" href="#">View Profile</a>
    </div>
    <p class="regulation">This firm is authorised and regulated by<br>the Legal Standards Authority, no.618203</p>
    <div class="partner partner-right">
      <h3>Peter Willett</h3>
      14 Orchard Lane<br>Ashbury<br>Hartshire AX7 2LM<br>Tel: 0300 555 0187
      <a class="btn" href="#">View Profile</a>
    </div>
    <div class="portrait" style="right:8px" role="img" aria-label="Black and white portrait photograph of Peter Willett"></div>
  </div>
</section>

<section class="expertise">
  <h2>Main Areas of Expertise</h2>
  <ul class="expertise-list" style="left:10px"><li>Company Matters</li><li>Commercial Matters</li><li>Commercial Crime</li><li>Litigation/Disputes</li></ul>
  <ul class="expertise-list" style="left:273px"><li>Insolvency</li><li>Residential Conveyancing</li><li>Commercial Conveyancing</li><li>Wills &amp; Probate</li></ul>
  <ul class="expertise-list" style="left:571px"><li>Estate Planning</li><li>Powers of Attorney</li><li>Care of the Elderly</li><li>Court of Protection</li></ul>
  <ul class="expertise-list" style="left:831px"><li>Divorce/Family</li><li>Pre-Nuptial Agreements</li><li>Intellectual Property</li><li>Media Law</li></ul>
</section>

<footer class="site-footer">
  <p class="legal">VAT registered number: 431 7720 95<br>Professional rules can be viewed on <a href="#">www.lsa-standards.example/code-of-conduct</a></p>
  <span class="member-badge" role="img" aria-label="Family law association membership badge"></span>
  <p class="footer-links"><a href="#">Legal Notices</a> | <a href="#">Privacy Policy</a></p>
  <p class="copyright">© DUNMORE &amp; WILLETT</p>
</footer>
</body>
</html>
```